Eye Catching Business Card for Optometrist

We've recently refreshed our logo and now we need a fresh and bold look for our business cards. We provide progressive ways to improve people's vision and protect their eye health.

Use our new logo as guidance into the colors to use. As far as style goes, I love how bold and eye catching the card is for Lanternfly Studio. Feel free to use your creative judgement.

Tagline: "Sharper sight for every day ahead."

pertinent info to include:

Dr. Martin Sowerby
Optometrist

2857 Bramwell Ridge Blvd #217
Quillmere, MO 64990
(555) 382-7190

marty@brightlenshomeoptics.example
www.brightlenshomeoptics.example

```html
<!DOCTYPE html>
<html lang="en">
<head>
<meta charset="utf-8">
<title>Bright Lens Home Optics — Business Card</title>
<link href="https://fonts.googleapis.com/css2?family=Oswald:wght@700&family=Open+Sans:wght@400;600;700&display=swap" rel="stylesheet">
<style>
  :root {
    --canvas: #e6e6e6;
    --card-white: #f7f7f5;
    --ink: #1c1c1c;
    --band: #3d3d3f;
    --band-text: #ffffff;
    --muted: #b9b9b9;
    --brand-red: #d3202a;
    --brand-tan: #d9bf9a;
    --text: #3a3a3a;
    --icon: #5a5a5a;
    --cream: #fbf3d2;
    --amber: #e9a43a;
    --rust: #c9682a;
  }
  * { box-sizing: border-box; margin: 0; padding: 0; }
  html, body { width: 1200px; height: 1200px; overflow: hidden; }
  body {
    background: var(--canvas);
    font-family: "Open Sans", Arial, sans-serif;
    display: flex;
    flex-direction: column;
    align-items: center;
    justify-content: center;
    gap: 80px;
  }
  .card {
    position: relative;
    width: 800px;
    height: 457px;
    overflow: hidden;
    box-shadow: 0 10px 30px rgba(0,0,0,.15);
  }

  /* Front */
  .card--front { background: var(--cream); }
  .front-texture {
    position: absolute; inset: 0;
    background: radial-gradient(ellipse at 38% 42%, var(--cream) 0%, #f6e3a6 40%, var(--amber) 78%, var(--rust) 100%);
  }
  .tagline {
    position: absolute; left: 56px; top: 92px;
    font-family: "Oswald", Impact, sans-serif;
    font-weight: 700;
    font-size: 27px;
    letter-spacing: .5px;
    color: var(--ink);
    text-transform: uppercase;
    white-space: nowrap;
  }
  .front-brand {
    position: absolute; right: 60px; bottom: 60px;
    display: flex; flex-direction: column; align-items: flex-end; gap: 16px;
  }
  .brand-square { width: 150px; height: 150px; background: var(--ink); }
  .brand-name {
    font-family: "Open Sans", Arial, sans-serif;
    font-weight: 700;
    color: var(--brand-red);
    text-transform: uppercase;
    line-height: 1.05;
    white-space: nowrap;
  }
  .front-brand .brand-name { font-size: 30px; text-align: right; }

  /* Back */
  .card--back { background: var(--card-white); }
  .band-stub {
    position: absolute; left: 0; top: 70px; width: 62px; height: 84px;
    background: var(--band);
  }
  .back-brand {
    position: absolute; left: 78px; top: 40px; width: 210px;
    display: flex; flex-direction: column; align-items: center; gap: 12px;
  }
  .back-brand .brand-square { width: 130px; height: 130px; background: var(--brand-tan); }
  .back-brand .brand-name { font-size: 22px; text-align: center; }
  .name-band {
    position: absolute; left: 300px; right: 0; top: 70px; height: 100px;
    background: var(--band);
    padding: 18px 0 0 28px;
  }
  .person-name { color: var(--band-text); font-weight: 700; font-size: 34px; line-height: 1.1; }
  .person-role { color: var(--muted); font-size: 19px; }
  .contact {
    position: absolute; left: 300px; top: 200px;
    list-style: none;
    color: var(--text);
    font-size: 21px;
    line-height: 1.35;
  }
  .contact li { display: flex; align-items: flex-start; gap: 10px; margin-bottom: 6px; white-space: nowrap; }
  .contact svg { flex: none; margin-top: 4px; }
  .contact .lines { display: flex; flex-direction: column; }
</style>
</head>
<body>

  <section class="card card--front">
    <div class="front-texture" role="img" aria-label="Warm grunge texture in cream, amber and rust tones"></div>
    <p class="tagline">"Sharper sight for every day ahead."</p>
    <div class="front-brand">
      <div class="brand-square"></div>
      <div class="brand-name">Bright Lens<br>Home Optics</div>
    </div>
  </section>

  <section class="card card--back">
    <div class="band-stub"></div>
    <div class="back-brand">
      <div class="brand-square"></div>
      <div class="brand-name">Bright Lens<br>Home Optics</div>
    </div>
    <div class="name-band">
      <p class="person-name">Dr. Martin Sowerby</p>
      <p class="person-role">Optometrist</p>
    </div>
    <ul class="contact">
      <li>
        <svg width="20" height="20" viewBox="0 0 20 20" aria-hidden="true"><circle cx="10" cy="10" r="10" fill="var(--icon)"/><path d="M10 4.5a3.5 3.5 0 0 0-3.5 3.5c0 2.6 3.5 7 3.5 7s3.5-4.4 3.5-7A3.5 3.5 0 0 0 10 4.5zm0 4.8a1.3 1.3 0 1 1 0-2.6 1.3 1.3 0 0 1 0 2.6z" fill="#fff"/></svg>
        <span class="lines"><span>2857 Bramwell Ridge Blvd #217</span><span>Quillmere, MO 64990</span></span>
      </li>
      <li>
        <svg width="20" height="20" viewBox="0 0 20 20" aria-hidden="true"><circle cx="10" cy="10" r="10" fill="var(--icon)"/><path d="M7 5h2l1 2.5-1.3 1a6 6 0 0 0 2.8 2.8l1-1.3L15 11v2a1 1 0 0 1-1 1A9 9 0 0 1 6 6a1 1 0 0 1 1-1z" fill="#fff"/></svg>
        <span>(555) 382-7190</span>
      </li>
      <li>
        <svg width="20" height="20" viewBox="0 0 20 20" aria-hidden="true"><circle cx="10" cy="10" r="10" fill="var(--icon)"/><rect x="5" y="6.5" width="10" height="7" fill="none" stroke="#fff" stroke-width="1.3"/><path d="M5 6.5l5 4 5-4" fill="none" stroke="#fff" stroke-width="1.3"/></svg>
        <span>marty@brightlenshomeoptics.example</span>
      </li>
      <li>
        <svg width="20" height="20" viewBox="0 0 20 20" aria-hidden="true"><circle cx="10" cy="10" r="10" fill="var(--icon)"/><circle cx="10" cy="10" r="5" fill="none" stroke="#fff" stroke-width="1.2"/><path d="M5 10h10M10 5c-2 2.7-2 7.3 0 10M10 5c2 2.7 2 7.3 0 10" fill="none" stroke="#fff" stroke-width="1.1"/></svg>
        <span>www.brightlenshomeoptics.example</span>
      </li>
    </ul>
  </section>

</body>
</html>
```